Travel Company is looking for a STAND OUT Business Card

I need a unique Business Card that will truly stand out. Nothing too busy. Simple is good, right? Not looking for a standard design either. No cookie cutter layout. We are a Travel Company that works more with Companies than Travelers. I had an idea to focus and emphasis on the 2 logo a bit more. This is not necessary, however thought it would look interesting. I am just looking for something interesting and a bit different. Does't have to completely off the wall crazy, just not your run of the mill business card.

Target Market(s)

Hoteliers, Resort Management, Call Centers, Executives, Travelers, Families, Businesses

Industry/Entity Type

Hospitality

Contact Information for Business Card

President/CEO - Marcus T Bellamy (title not necessary if design doesn't allow for it)
contact - (407) 555-0186
email - mbellamy@wayfarenow.example
address - 4812 Quillmore Ave #164
Orlando, FL 32804
website - www.wayfarenow.example

Font styles to use
Serif
Other font styles liked:
• Avenir Next LT Pro BOLD

Requirements
Must have
• simple look and design. Unique design
Nice to have
• I attached the 2 logo separate from the main logo. This can be used separately from the Main Logo, together with the main logo or as main logo. I included the logo font. Use it or not, designers choice.
Should not have
• cookie cutter design. Little use of red other than the logo

```html
<!DOCTYPE html>
<html lang="en">
<head>
<meta charset="utf-8">
<title>wayfarenow — Business Card</title>
<link href="https://fonts.googleapis.com/css2?family=Open+Sans:wght@600;700;800&family=Roboto:wght@400;500&display=swap" rel="stylesheet">
<style>
  :root {
    --backdrop: #9e9b9c;
    --paper: #fbfbfb;
    --ink: #231f20;
    --ink-soft: #2e2e2e;
    --band: #141517;
    --accent: #d7282c;
  }
  * { margin: 0; padding: 0; box-sizing: border-box; }
  html, body { width: 1200px; height: 1200px; overflow: hidden; }
  body {
    background: var(--backdrop);
    position: relative;
    font-family: "Roboto", Arial, sans-serif;
    color: var(--ink);
  }
  .card {
    position: absolute;
    background: var(--paper);
    overflow: hidden;
  }
  .card--front { left: 238px; top: 119px; width: 712px; height: 418px; }
  .card--back  { left: 231px; top: 644px; width: 711px; height: 417px; }

  .brand {
    display: flex;
    align-items: center;
    gap: 12px;
    font-family: "Open Sans", Arial, sans-serif;
    font-weight: 800;
    color: var(--ink);
    letter-spacing: -1px;
  }
  .brand__dot {
    border-radius: 50%;
    background: var(--accent);
    flex: none;
  }
  .card--front .brand {
    position: absolute;
    left: 50%; top: 50%;
    transform: translate(-50%, -50%);
    font-size: 52px;
  }
  .card--front .brand__dot { width: 22px; height: 22px; }

  .card__band {
    position: absolute; left: 0; top: 0; bottom: 0;
    width: 57px; background: var(--band);
  }
  .card__stripe {
    position: absolute; left: 59px; top: 0; bottom: 0;
    width: 7px; background: var(--accent);
  }
  .card--back .brand {
    position: absolute;
    right: 47px; top: 62px;
    font-size: 42px;
  }
  .card--back .brand__dot { width: 17px; height: 17px; }

  .holder { position: absolute; left: 92px; top: 38px; }
  .holder__name {
    font-family: "Open Sans", Arial, sans-serif;
    font-weight: 700;
    font-size: 25px;
    color: var(--ink-soft);
  }
  .holder__title { font-size: 15px; margin-top: 2px; color: var(--ink-soft); }

  .contacts {
    position: absolute; left: 92px; top: 276px;
    list-style: none;
    font-size: 17px;
    color: var(--ink-soft);
  }
  .contacts__item {
    display: flex; align-items: center; gap: 16px;
    height: 25.5px;
  }
  .contacts__icon { width: 16px; height: 16px; fill: var(--accent); flex: none; }
  .contacts__address { margin-top: 4px; padding-left: 0; }
</style>
</head>
<body>

<section class="card card--front">
  <div class="brand"><span class="brand__dot"></span>wayfarenow</div>
</section>

<section class="card card--back">
  <div class="card__band"></div>
  <div class="card__stripe"></div>

  <div class="holder">
    <h1 class="holder__name">Marcus T Bellamy</h1>
    <p class="holder__title">President/CEO</p>
  </div>

  <div class="brand"><span class="brand__dot"></span>wayfarenow</div>

  <ul class="contacts">
    <li class="contacts__item">
      <svg class="contacts__icon" viewBox="0 0 16 16" aria-hidden="true"><path d="M2 5c0-2 2-3 6-3s6 1 6 3v1h-3V5H5v1H2zM4 7h8l2 6H2zM8 9a1.5 1.5 0 1 0 0 3 1.5 1.5 0 0 0 0-3z"/></svg>
      (407) 555-0186
    </li>
    <li class="contacts__item">
      <svg class="contacts__icon" viewBox="0 0 16 16" aria-hidden="true"><path d="M8 1a7 7 0 1 0 0 14A7 7 0 0 0 8 1zm0 1.5c.8 0 1.7 1.5 2 3.7H6c.3-2.2 1.2-3.7 2-3.7zM2.6 7.3h2.3a12 12 0 0 0 0 1.4H2.6a5.6 5.6 0 0 1 0-1.4zm3.5 0h3.8a11 11 0 0 1 0 1.4H6.1a11 11 0 0 1 0-1.4zm5 0h2.3a5.6 5.6 0 0 1 0 1.4h-2.3a12 12 0 0 0 0-1.4zM6 9.8h4c-.3 2.2-1.2 3.7-2 3.7s-1.7-1.5-2-3.7z"/></svg>
      www.wayfarenow.example
    </li>
    <li class="contacts__item">
      <svg class="contacts__icon" viewBox="0 0 16 16" aria-hidden="true"><path d="M1 3h14v1.2L8 9 1 4.2zM1 5.6l7 4.8 7-4.8V13H1z"/></svg>
      mbellamy@wayfarenow.example
    </li>
    <li class="contacts__item contacts__address">4812 Quillmore Ave #164 Orlando, FL 32804</li>
  </ul>
</section>

</body>
</html>
```